KORBALT

The business want a professional looking business card. We have a scetch we will add but want the extra upgrade, and would like more suggestions for variations of our business cards.

```html
<!DOCTYPE html>
<html lang="en">
<head>
<meta charset="utf-8">
<title>KORBALT Business Card</title>
<link rel="stylesheet" href="https://fonts.googleapis.com/css2?family=Playfair+Display:wght@500;700&family=Quicksand:wght@400;500&display=swap">
<style>
  :root {
    --backdrop: #1c1c1c;
    --card: #141414;
    --gold: #dcae3c;
    --gold-light: #f3d67e;
    --gold-deep: #a8781c;
  }
  * { margin: 0; padding: 0; box-sizing: border-box; }
  html, body {
    width: 1062px;
    height: 1200px;
    overflow: hidden;
    background: var(--backdrop);
  }
  .canvas { position: relative; width: 1062px; height: 1200px; }
  .card {
    position: absolute;
    left: 146px;
    width: 754px;
    height: 430px;
    background: var(--card);
    border-radius: 18px;
    overflow: hidden;
  }
  .card--front { top: 60px; }
  .card--back { top: 590px; }

  /* Front */
  .brand {
    position: absolute;
    left: 0; right: 0;
    top: 120px;
    text-align: center;
    color: var(--gold);
  }
  .brand__dot {
    display: block;
    width: 74px;
    height: 74px;
    margin: 0 auto 46px;
    border-radius: 50%;
    background: var(--gold);
  }
  .brand__name {
    font-family: "Playfair Display", serif;
    font-weight: 500;
    font-size: 30px;
    letter-spacing: 14px;
    padding-left: 14px;
    line-height: 1;
  }
  .brand__since {
    margin-top: 14px;
    font-family: "Quicksand", sans-serif;
    font-weight: 500;
    font-size: 14px;
    letter-spacing: 1.5px;
  }

  /* Back */
  .decoration {
    position: absolute;
    right: -140px;
    top: -40px;
    width: 480px;
    height: 520px;
    border-radius: 50% 0 0 50%;
    background: radial-gradient(circle at 40% 50%, var(--gold-light) 0%, var(--gold) 45%, var(--gold-deep) 100%);
    opacity: 0.9;
  }
  .identity {
    position: absolute;
    left: 42px;
    top: 162px;
    color: var(--gold);
  }
  .identity__company {
    font-family: "Playfair Display", serif;
    font-weight: 700;
    font-size: 28px;
    line-height: 1;
    color: var(--gold-light);
  }
  .identity__person {
    margin-top: 8px;
    font-family: "Quicksand", sans-serif;
    font-weight: 500;
    font-size: 19px;
    letter-spacing: 0.3px;
  }
  .identity__role {
    margin-top: 4px;
    padding-left: 4px;
    font-family: "Quicksand", sans-serif;
    font-size: 17px;
    color: var(--gold-light);
  }
  .divider {
    position: absolute;
    left: 44px;
    top: 256px;
    width: 384px;
    height: 1.5px;
    background: var(--gold);
  }
  .contacts {
    position: absolute;
    left: 58px;
    top: 280px;
    list-style: none;
    font-family: "Quicksand", sans-serif;
    font-size: 22px;
    color: var(--gold-light);
  }
  .contacts__item {
    display: flex;
    align-items: center;
    height: 38px;
  }
  .contacts__icon {
    width: 18px;
    height: 18px;
    margin-right: 24px;
    fill: none;
    stroke: var(--gold-light);
    stroke-width: 1.6;
    stroke-linejoin: round;
    stroke-linecap: round;
  }
</style>
</head>
<body>
<main class="canvas">
  <section class="card card--front">
    <div class="brand">
      <span class="brand__dot"></span>
      <div class="brand__name">KORBALT</div>
      <div class="brand__since">SINCE 2026</div>
    </div>
  </section>

  <section class="card card--back">
    <div class="decoration" role="img" aria-label="Large gold foil ornamental leaf pattern filling the right edge"></div>
    <div class="identity">
      <div class="identity__company">KORBALT SOLBERG</div>
      <div class="identity__person">ANDERS MIKAEL SOLBERG</div>
      <div class="identity__role">ceo &amp; founder</div>
    </div>
    <div class="divider"></div>
    <ul class="contacts">
      <li class="contacts__item">
        <svg class="contacts__icon" viewBox="0 0 24 24" aria-hidden="true"><path d="M5 3h4l2 5-2.5 1.5a11 11 0 0 0 6 6L16 13l5 2v4a2 2 0 0 1-2 2A16 16 0 0 1 3 5a2 2 0 0 1 2-2z"/></svg>
        <span>004795550142</span>
      </li>
      <li class="contacts__item">
        <svg class="contacts__icon" viewBox="0 0 24 24" aria-hidden="true"><rect x="2" y="5" width="20" height="14" rx="1.5"/><path d="M2 6l10 7 10-7"/></svg>
        <span>korbalt.llc@mailbox.com</span>
      </li>
      <li class="contacts__item">
        <svg class="contacts__icon" viewBox="0 0 24 24" aria-hidden="true"><path d="M5 2l14 11-6 1 3 7-3 1-3-7-5 4z"/></svg>
        <span>www.korbalt.llc</span>
      </li>
    </ul>
  </section>
</main>
</body>
</html>
```